MOSLEN Environmental needs an upgrade to its current business cards design

We need an upgrade to our current business cards design, where the MOSLEN acronym is included, as possible and not being overloaded.
MOSLEN Environmental is an Environmental Consultancy Firm based in Sydney.
We would like to see creative designs different from the standard type of business cards (for example, rounded edges, different to standard size of common business cards.

Target Market(s)

industrial companies (oil & gas, petrochemical, mining, insolvency, finance and manufacturing), developers, architect firms, law firms.

Industry/Entity Type

Business

Contact Information for Business Card

logos (brand and acronym), if they don't appear overloaded.
name
role
name of company (MOSLEN Environmental),
address (Level 3, Suite 3C, 47-49 Dorrigan Lane, Wexmoor, NSW, 2188) landline (02 7314 2986)
mobile (staff member)
email (staff member) and
website (www.moslengreen.example).
Include: Contaminated Land, Site Remediation, Groundwater Assessment, Health and Ecological Risk Assessments, Acid Sulfate Soils, Waste Classification.

Font styles to use
Serif
Sans Serif

Requirements
Must have
• A creative design different to the standard type of business cards.
Nice to have
• Rounded edges
• Different size of business cards rather than the standard size.
Should not have
• Preferable not to use white colour background, unless it is required from a creative design proposed.
• Not an overloaded design.
• Avoid black colours

```html
<!DOCTYPE html>
<html lang="en">
<head>
<meta charset="utf-8">
<title>MOSLEN Environmental – Business Card</title>
<link href="https://fonts.googleapis.com/css2?family=Lato:wght@400;700;900&display=swap" rel="stylesheet">
<style>
  :root {
    --page-bg: #222222;
    --card-bg: #1c1c1c;
    --card-edge: #3a3a3a;
    --green: #7dc242;
    --grey: #7a7a7a;
    --grey-dark: #6a6a6a;
  }
  html, body {
    margin: 0;
    padding: 0;
    width: 1189px;
    height: 1200px;
    overflow: hidden;
    background: var(--page-bg);
    font-family: "Lato", Arial, sans-serif;
  }
  .canvas { position: relative; width: 1189px; height: 1200px; }
  .card {
    position: absolute;
    left: 171px;
    width: 855px;
    height: 487px;
    background: var(--card-bg);
    border-top: 1px solid var(--card-edge);
    border-radius: 2px 16px 16px 2px;
    box-shadow: 0 6px 14px rgba(0,0,0,0.55);
  }
  .card--front { top: 68px; }
  .card--back { top: 627px; }

  .wordmark { position: absolute; color: var(--green); font-weight: 900; line-height: 1; text-align: center; }
  .wordmark__name { display: block; }
  .wordmark__tag { display: block; }

  .card--front .wordmark { left: 0; right: 0; top: 72px; }
  .card--front .wordmark__name { font-size: 104px; letter-spacing: 0.02em; }
  .card--front .wordmark__tag { font-size: 34px; letter-spacing: 0.2em; margin-top: 14px; }

  .services { position: absolute; left: 0; right: 0; top: 288px; text-align: center; }
  .services__title { margin: 0 0 18px; color: var(--green); font-size: 29px; font-weight: 700; }
  .services__list { margin: 0; color: var(--grey); font-size: 23px; line-height: 29px; }

  .card--back .wordmark { left: 48px; width: 340px; top: 186px; }
  .card--back .wordmark__name { font-size: 80px; letter-spacing: 0.02em; }
  .card--back .wordmark__tag { font-size: 26px; letter-spacing: 0.17em; margin-top: 10px; }

  .contact { position: absolute; left: 467px; top: 64px; color: var(--grey); font-size: 24px; }
  .contact__name { margin: 0; color: var(--green); font-size: 30px; font-weight: 700; line-height: 34px; letter-spacing: 0.01em; }
  .contact__role { margin: 0; line-height: 32px; }
  .contact__address { margin: 22px 0 0 2px; font-style: normal; line-height: 34px; }
  .contact__lines { list-style: none; margin: 10px 0 0 2px; padding: 0; line-height: 33px; }
  .contact__lines li { display: flex; align-items: center; gap: 10px; }
  .contact__lines svg { width: 22px; height: 22px; fill: var(--green); flex: none; }
  .contact__web { margin: 22px 0 0; line-height: 32px; }
  .contact__web span { color: var(--green); }
</style>
</head>
<body>
<div class="canvas">

  <section class="card card--front">
    <div class="wordmark">
      <span class="wordmark__name">MOSLEN</span>
      <span class="wordmark__tag">ENVIRONMENTAL</span>
    </div>
    <div class="services">
      <h2 class="services__title">WHAT WE DO:</h2>
      <p class="services__list">
        Contaminated Land | Site Remediation | Groundwater Assessment<br>
        Health and Ecological Risk Assessments | Acid Sulfate Soils<br>
        Waste Classification.
      </p>
    </div>
  </section>

  <section class="card card--back">
    <div class="wordmark">
      <span class="wordmark__name">MOSLEN</span>
      <span class="wordmark__tag">ENVIRONMENTAL</span>
    </div>
    <div class="contact">
      <h1 class="contact__name">NOLAN VERRICK</h1>
      <p class="contact__role">Project Engineer</p>
      <address class="contact__address">
        Level 3, Suite 3C<br>
        47-49 Dorrigan Lane,<br>
        Wexmoor, NSW, 2188
      </address>
      <ul class="contact__lines">
        <li>
          <svg viewBox="0 0 24 24" aria-hidden="true"><path d="M3 9c0-3 4-5 9-5s9 2 9 5v2h-5V9c-1-.6-2.5-1-4-1s-3 .4-4 1v2H3z"/><path d="M6 13h12l2 7H4z"/></svg>
          02 7314 2986
        </li>
        <li>
          <svg viewBox="0 0 24 24" aria-hidden="true"><path d="M8 2h8a2 2 0 0 1 2 2v16a2 2 0 0 1-2 2H8a2 2 0 0 1-2-2V4a2 2 0 0 1 2-2zm0 3v7h8V5zm1 9v2h2v-2zm4 0v2h2v-2zm-4 3v2h2v-2zm4 0v2h2v-2z"/></svg>
          0412 688 305
        </li>
        <li>
          <svg viewBox="0 0 24 24" aria-hidden="true"><path d="M2 5h20v14H2zm2 2v.5l8 6 8-6V7zm0 3v7h16v-7l-8 6z"/></svg>
          nolan@moslengreen.example
        </li>
      </ul>
      <p class="contact__web">www.<span>moslengreen</span>.example</p>
    </div>
  </section>

</div>
</body>
</html>
```